Zielgruppe
brinko handel ist eine Vertriebsagentur, die sich ausschließlich auf den BtoB Vertrieb spezialisiert hat. Wir agieren seit 19 Jahren am Markt und sind mehrfach ausgezeichneter Exzellenzberater des Mittelstandes. Wir unterstützen mittelständische Unternehmen, Familienunternehmen, Start up´s in der Wachstumsphase und Großkonzerne in der Industrie und im Dienstleistungsbereich. Ansprechpartner für uns sind Vertriebsleiter und GF´s in den Unternehmen.
Aufgabenstellung
Wir möchten unsere Angebotsvorlage neu im Layout neu designen lassen. Sie soll unsere Arbeitsweise zielgenau - authentisch - pfiffig widerspiegeln. Ich möchte gerne eine moderne und klare Struktur. Auf einer Seite sollen unsere USP´s dargestellt werden und auf ein - zwei Seiten ist das Angebot - in den folgenden Seiten sind die Vertragsinhalte.

```html
<!DOCTYPE html>
<html lang="de">
<head>
<meta charset="utf-8">
<title>brinko handel – Angebotsvorlage</title>
<link href="https://fonts.googleapis.com/css2?family=Days+One&family=Jost:wght@400;500;600;700&family=Lora:wght@400&display=swap" rel="stylesheet">
<style>
  :root{
    --dark:#58595b;
    --blue:#1e9bd7;
    --grey:#9c9c9c;
    --icon:#8e8e8e;
    --text:#3a3a3a;
    --paper:#ffffff;
  }
  *{box-sizing:border-box;margin:0;padding:0}
  html,body{width:1200px;height:4240px;overflow:hidden;background:var(--paper)}
  body{position:relative;font-family:'Jost',sans-serif;color:var(--text)}
  .page{position:absolute;width:600px;overflow:hidden}
  .abs{position:absolute}
  .band{position:absolute;left:0;width:600px;height:90px;background:var(--dark);display:flex;align-items:center;justify-content:center;font-family:'Days One',sans-serif;color:var(--blue);font-size:31px;letter-spacing:.5px}
  .display{font-family:'Days One',sans-serif;color:var(--blue)}
  .para{font-size:10.5px;line-height:1.45}
  .para h4{font-weight:500;color:var(--blue);font-size:10.5px;margin-top:10px}
  .para h4 .sec{font-size:18px;font-weight:600;margin-right:3px}
  .para p{margin:0}

  /* cover */
  .cover{left:600px;top:0;height:650px;background:var(--dark)}
  .cover-title{top:72px;width:100%;text-align:center;font-size:40px}
  .cover-photo{left:116px;top:175px;width:368px;height:368px;border-radius:50%;background:radial-gradient(circle at 45% 40%,#d9d4cf,#8a857f 70%,#5a5553)}
  .brand{left:600px;top:735px;width:600px;text-align:center}
  .brand-name{font-size:46px;font-weight:500;color:var(--blue);letter-spacing:1px;line-height:1}

  /* USP page */
  .usp{left:0;top:840px;height:748px}
  .usp-photo{left:230px;top:0;width:370px;height:213px;background:linear-gradient(135deg,#f4f4f4 0%,#dcdcdc 55%,#f7f7f7 100%)}
  .usp-box{left:0;top:44px;width:230px;height:573px;background:var(--dark);padding:20px 18px 0 28px;color:#fff}
  .usp-box h3{font-family:'Days One',sans-serif;color:var(--blue);font-size:15.5px;line-height:1.22;font-weight:400}
  .usp-box p{font-size:14px;line-height:1.42;margin-top:22px;text-align:justify}
  .usp-head{left:250px;top:183px;font-size:20px;font-weight:500;color:var(--blue)}
  .usp-item{position:absolute;width:104px;text-align:center}
  .usp-item .dot{width:34px;height:34px;border-radius:50%;background:var(--icon);margin:0 auto 10px}
  .usp-item b{display:block;font-size:11.5px;font-weight:500;color:var(--blue);line-height:1.1}
  .usp-item span{display:block;font-size:8.5px;line-height:1.45;margin-top:5px}

  /* offer page */
  .offer{left:600px;top:840px;height:748px}
  .offer h3{position:absolute;left:30px;font-family:'Days One',sans-serif;color:var(--blue);font-size:21px;font-weight:400}
  .offer .lines{position:absolute;left:30px;font-size:11.5px;line-height:1.6}
  .project{left:47px;top:241px;width:512px;height:265px;border:1.5px solid var(--blue);padding:12px 14px}
  .project h2{font-family:'Days One',sans-serif;color:var(--blue);font-size:20px;font-weight:400}
  .project p,.project li{font-size:7.5px;line-height:1.55}
  .project ul{list-style:none;margin:12px 0 10px 26px}
  .offer-summary{left:0;top:540px;width:600px;text-align:center;font-size:11px;line-height:1.85}
  .offer-summary .hi{color:var(--blue);font-weight:500}
  .offer-summary .gap{margin-top:16px}

  /* order form */
  .form{left:0;top:1597px;height:847px}
  .form-scene{left:0;top:90px;width:600px;height:757px;background:linear-gradient(160deg,#f1f2f2 0%,#ffffff 40%,#ffffff 100%)}
  .form-sheet{left:14px;top:325px;width:560px;height:522px;background:#fff;border-left:14px solid #e3e6e6}
  .form-text{left:90px;font-size:15px;line-height:1.2}
  .form-text b{font-weight:600}
  .rule{display:inline-block;border-bottom:1px solid var(--text);height:1px;vertical-align:baseline}

  /* contract page 1 */
  .contract{left:600px;top:1597px;height:847px}
  .parties{left:0;top:93px;width:600px;height:216px;background:var(--dark);color:#fff}
  .parties h3{font-family:'Days One',sans-serif;color:var(--blue);font-size:20px;font-weight:400}
  .parties p{font-size:12px;line-height:1.9}
  .col{position:absolute;width:180px}

  /* contract page 2 */
  .confirm{left:0;top:2449px;height:848px}
  .placeholder{left:0;top:94px;width:600px;height:239px;background:var(--grey);color:#f2f2f2;font-family:'Lora',serif;font-size:28px;padding:88px 0 0 94px}

  .terms{left:600px;top:2449px;height:848px}
  .deco-flowers{left:420px;top:90px;width:180px;height:225px;background:radial-gradient(circle at 60% 45%,#fdfdf4 0%,#e7eed8 45%,#ffffff 80%)}
  .deco-pot{left:430px;top:360px;width:170px;height:210px;border-radius:48% 0 0 48%;background:radial-gradient(circle at 45% 50%,#bfe3df,#9dd1cc 60%,#ffffff 100%)}
  .deco-note{left:442px;top:582px;width:92px;height:172px;background:#fafafa;border-right:8px solid #9fd2cc;box-shadow:0 0 0 1px #ececec}
  .terms-text{left:37px;top:250px;width:372px;font-size:10.5px;line-height:1.45}
  .terms-text p{margin-top:10px}
  .sign{left:37px;font-size:11px;font-weight:600}

  /* profile page */
  .profile{left:0;top:3297px;height:943px}
  .profile-photo{left:0;top:91px;width:600px;height:365px;background:linear-gradient(120deg,#3c3a38 0%,#8c8884 40%,#e8e6e3 60%,#bcb7b1 100%)}
  .profile-lead{left:41px;top:478px;font-size:12.5px;font-weight:600;color:var(--blue)}
  .circle{position:absolute;top:528px;width:50px;height:50px;border-radius:50%;background:var(--icon)}
  .profile-list{left:41px;top:595px;width:540px;font-size:10.5px;line-height:1.85}
  .profile-list .hi{color:var(--blue)}
  .profile-list .in{padding-left:8px}
  .portrait{left:400px;top:770px;width:162px;height:162px;border-radius:50%;background:var(--grey);display:flex;align-items:center;justify-content:center;font-family:'Lora',serif;font-size:12px;color:#333;z-index:2}
  .footer{left:0;top:876px;width:600px;height:67px;background:var(--dark)}
  .footer .name{position:absolute;left:0;width:380px;top:13px;text-align:center;font-size:22px;font-weight:500;color:var(--blue);line-height:1}
  .footer .addr{position:absolute;left:0;width:380px;top:44px;text-align:center;font-size:9px;color:#fff}
</style>
</head>
<body>

<!-- Cover -->
<section class="page cover">
  <h1 class="abs cover-title display" style="font-weight:400">Hier steht z.B.ein Titel</h1>
  <div class="abs cover-photo" role="img" aria-label="Foto: drei Geschäftsleute im Gespräch am Tisch, runder Bildausschnitt"></div>
</section>
<div class="abs brand">
  <div class="brand-name">brinko handel</div>
</div>

<!-- USP page -->
<section class="page usp">
  <div class="abs usp-photo" role="img" aria-label="Foto: Laptop, Kaffeetasse und Notizblock auf weißem Schreibtisch"></div>
  <div class="abs usp-box">
    <h3>brinko handel – seit 19 Jahren am Markt – hat sich auf die Kaltakquise und den Vertrieb im BtoB-Bereich spezialisiert –</h3>
    <p>Wir sind der Turbo für Ihren Vertrieb und gehören zu den 10 führenden Anbietern im B2B-Vertrieb. Wir bewegen uns sicher in der Akquise in der oberen Führungsebene bis zum DAX-Konzern. Wir bieten eine 720° strukturierte Vertriebsberatung, -umsetzung und -kontrolle: von A (Analyse) – Z (Verkauf). Wir denken vor und zurück, reflektieren Gespräche und Zielgruppe.</p>
    <p>Wir sind zum 3. Mal in Folge als Exzellenzberater Deutscher Mittelstand im Vertrieb ausgezeichnet!</p>
  </div>
  <div class="abs usp-head">IHRE VORTEILE</div>

  <div class="usp-item" style="left:248px;top:232px"><div class="dot"></div><b>ENTSCHEIDER</b><span>Wir führen 12.000 Gespräche im Monat mit Vorständen, Geschäftsführern, Marketing-, Vertriebs- und Einkaufsleitern</span></div>
  <div class="usp-item" style="left:356px;top:232px"><div class="dot"></div><b>RICHTIGER ZEITPUNKT</b><span>Wir haben das Fingerspitzengefühl beim Interessenten zum richtigen Zeitpunkt der Entscheidung präsent zu sein, ohne penetrant zu wirken</span></div>
  <div class="usp-item" style="left:465px;top:232px"><div class="dot"></div><b>VERTRIEBSAFFIN</b><span>Kompetenz und vor allem Erfahrungen im Vertrieb lassen uns schnell und zielsicher für Sie agieren. Wir wissen wie wir die richtigen Ansprechpartner kontaktieren und auch begeistern können.</span></div>

  <div class="usp-item" style="left:248px;top:396px"><div class="dot"></div><b>ENTSCHEIDER</b><span>Wir führen 12.000 Gespräche im Monat mit Vorständen, Geschäftsführern, Marketing-, Vertriebs- und Einkaufsleitern</span></div>
  <div class="usp-item" style="left:356px;top:413px"><div class="dot"></div><b>ENTSCHEIDER</b><span>Wir führen 12.000 Gespräche im Monat mit Vorständen, Geschäftsführern, Marketing-, Vertriebs- und Einkaufsleitern</span></div>
  <div class="usp-item" style="left:465px;top:470px"><b>ENTSCHEIDER</b><span>Wir führen 12.000 Gespräche im Monat mit Vorständen, Geschäftsführern, Marketing-, Vertriebs- und Einkaufsleitern</span></div>

  <div class="usp-item" style="left:248px;top:563px"><div class="dot"></div><b>ENTSCHEIDER</b><span>Wir führen 12.000 Gespräche im Monat mit Vorständen, Geschäftsführern, Marketing-, Vertriebs- und Einkaufsleitern</span></div>
  <div class="usp-item" style="left:356px;top:620px"><b>ENTSCHEIDER</b><span>Wir führen 12.000 Gespräche im Monat mit Vorständen, Geschäftsführern, Marketing-, Vertriebs- und Einkaufsleitern</span></div>
</section>

<!-- Offer page -->
<section class="page offer">
  <h3 style="top:24px">SETUP-Installation einmalig</h3>
  <div class="lines" style="top:64px">2 h Workshop – Einweisung Mitarbeiterin 2h (1)<br>Abstimmung Prozesse und Schnittstellen<br>Erarbeitung + Coaching Gesprächskonzept / Einwandargumentation</div>
  <h3 style="top:141px">TECHNIK-Programmierung einmalig</h3>
  <div class="lines" style="top:178px">Integration firmeninterner Telefonnummer</div>

  <div class="abs project">
    <h2>PROJEKTARBEIT</h2>
    <p style="margin-top:6px">agieren unter Nordhafen Spedition SE &amp; Co. KG<br>akquirieren auf Entscheiderebene in den Unternehmen Einkauf, Qualitätsmanager, Produktionsleiter stellen das Unternehmen mit seinen Dienstleistungen und Vorteilen vor und erfragen</p>
    <ul>
      <li>- aktuellen Bedarf an Logistik</li>
      <li>- wiederkehrende und herausfordernde Destinationen inkl. Tonnagen</li>
      <li>- Zufriedenheit mit dem aktuellen Partner evaluieren die aktuelle IST-Situation und erfragen ggf. bestehende Partnerschaften / Verträge wecken Interesse an den Dienstleistungen und bauen ein vertrauensvolles Verhältnis auf</li>
      <li>- erarbeiten bedarfsorientierte Wiedervorlagen,</li>
      <li>- koordinieren und bestätigen Termine vor Ort,</li>
      <li>- bleiben am vertriebsorientiert dran Kontakt,</li>
      <li>- erfragen Alternativangebote</li>
    </ul>
    <p>telefonieren aktiv Angeboten nach und erfragen die Entscheidergründe</p>
  </div>

  <div class="abs offer-summary">
    <div class="hi">Adressrecherche / Adressdaten inkl. Kontaktdaten</div>
    <div>Adressselektion nach Unternehmen, Branchen und Regionen</div>
    <div class="hi gap">a ) TESTPROJEKT - 15h/ Woche – 10 Wochen</div>
    <div>14h Akquise/ Recherche + 2h interne Projektabstimmung je Woche<br>garantiert 140 Gespräche / Woche</div>
    <div class="hi gap">b ) TESTPROJEKT - 20h / Woche – 10 Wochen</div>
    <div>18,5h Akquise/ Recherche + 1,5h interne Projektabstimmung je Woche garantiert 185 Gespräche / Woche</div>
  </div>
</section>

<!-- Order form -->
<section class="page form">
  <div class="band" style="top:0">NEUE MÄRKTE EROBERN</div>
  <div class="abs form-scene" role="img" aria-label="Foto: Laptop, Kaffeetasse und Spiralblock auf hellem Schreibtisch als Hintergrund des Formulars"></div>
  <div class="abs form-sheet"></div>
  <div class="abs form-text" style="top:203px"><b>Auftraggeber</b><br>Nordhafen Spedition SE &amp; Co. KG</div>
  <div class="abs form-text" style="top:305px"><b>Auftragnehmer</b><br>brinko handel GmbH<br>Lindenweg 7<br>90402 Nürnberg</div>
  <div class="abs form-text" style="top:408px;width:460px">Hiermit bestätige ich als Auftraggeber das Angebot-Nr. 20221108 und erteile entsprechend dem Angebot den Auftrag an brinko handel GmbH.</div>
  <div class="abs form-text" style="left:163px;top:493px">Variante a - 15h Vertriebsunterstützung / Woche<br>Variante b - 20h Vertriebsunterstützung / Woche</div>
  <div class="abs form-text" style="top:580px">Ort, Datum: <span class="rule" style="width:395px"></span></div>
  <div class="abs form-text" style="top:666px">Name/Vorname in Druckbuchstaben: <span class="rule" style="width:232px"></span></div>
  <div class="abs form-text" style="top:717px">Unterschrift: <span class="rule" style="width:385px"></span></div>
  <div class="abs form-text" style="top:800px">Firmenstempel <span class="rule" style="width:375px"></span></div>
</section>

<!-- Contract page 1 -->
<section class="page contract">
  <div class="band" style="top:0">NEUE KUNDEN AKQUIRIEREN</div>
  <div class="abs parties">
    <div class="abs" style="left:37px;top:30px"><h3>Auftraggeber</h3><p style="line-height:1.4">Nordhafen Spedition SE &amp; Co. KG</p></div>
    <div class="abs" style="left:399px;top:65px"><h3>Auftragnehmer</h3><p>brinko handel GmbH<br>Marlen Voss<br>Lindenweg 7<br>90402 Nürnberg</p></div>
  </div>
  <div class="col para" style="left:37px;top:325px">
    <h4 style="margin-top:0"><span class="sec">§ 1</span>Vertragsgegenstand</h4>
    <p>Der AN unterstützt den AG bei der Akquise neuer Kunden.</p>
    <h4><span class="sec">§ 2</span>Leistungen/ Vergütung des AN</h4>
    <p>Siehe Seite LEISTUNGEN</p>
    <h4><span class="sec">§ 3</span>Pflichten des AG</h4>
    <p>(1) Der AG verpflichtet sich, dem AN rechtzeitig, vollständig und korrekt die zur Ausübung seiner Tätigkeit erforderlichen Unterlagen, Druckerzeugnisse u. / o. vorkonfektionierte Briefumschläge zum Versand an die Interessenten inkl. Porto, unentgeltlich zur Verfügung zu stellen.</p>
    <p>(2) Der AG schuldet sämtliche für die Durchführung der o.g. Leistungen des AN notwendigen Informationen.</p>
    <p>(3) Der AG hat dem AN Zugang zu seiner Kundenkartei zu Akquisezwecken zu gewähren. Der AG sichert zu, dass er die Gewähr dafür übernimmt, dass</p>
  </div>
  <div class="col para" style="left:228px;top:325px">
    <p>bei dem gesamten von ihm zur Verfügung gestellten Adressen eine telefonische Kontaktaufnahme mit dem Kunden/ Nichtkunden gestattet ist.</p>
    <h4><span class="sec">§ 4</span>Zahlungsvereinbarung</h4>
    <p>(1) Der AN erhält für seine Tätigkeit eine Pauschalvergütung wie in § 2 definiert zzgl. gesetzl. MwSt.</p>
    <p>(2) Der in Rechnung gestellte Betrag ist innerhalb von 14 Tagen ab dem Rechnungsdatum ohne Bank- verbindungen ohne Abzüge zu überweisen.</p>
    <p>(3) Verrechnungsschecks werden nicht akzeptiert.</p>
    <p>(4) jährliche Kostenanpassung anhand des Arbeitskostenindex - Der vereinbarte Pauschalpreis je Monat wird im Folgejahr im Januar entsprechend der Entwicklung des Arbeitskostenindex angepasst. Die Entwicklung des Arbeitskostenindex laut Statistischen Bundesamt wird entsprechend der prozentualen Veränderung berechnet.</p>
  </div>
  <div class="col para" style="left:420px;top:325px">
    <h4 style="margin-top:0"><span class="sec">§ 5</span>Vertragsdauer, Vertragsende</h4>
    <p>(1) Dieser Vertrag hat eine feste Laufzeit von 10 Wochen ab Beginn Workshop. Er verlängert er sich stillschweigend jeweils um 3 Monate, wenn er nicht von einem der Vertragspartner mit einer Frist von 1 Woche zum Vertragsende schriftlich gekündigt wird.</p>
    <p>(2) Der AG erhält ein Sonderkündigungsrecht nach 3 Wochen der Zusammenarbeit innerhalb 1 Woche.</p>
    <p>(3) Das Recht zur Kündigung aus wichtigem Grund bleibt unberührt. Der AN ist zur Kündigung aus wichtigem Grund berechtigt, wenn der AG mit der Zahlung der Vergütung gemäß § 5 dieses Vertrags mit mehr als zwei Wochen in Rückstand gerät.</p>
  </div>
</section>

<!-- Contract page 2 -->
<section class="page confirm">
  <div class="band" style="top:0">ANGEBOTSBESTÄTIGUNG</div>
  <div class="abs placeholder">TEXT ODER BILD MÖGLICH</div>
  <div class="col para" style="left:36px;top:361px">
    <h4 style="margin-top:0"><span class="sec">§ 6</span>Haftung</h4>
    <p>(1) Der AN haftet unbeschränkt bei Vorsatz oder grober Fahrlässigkeit, für die Verletzung von Leben, Leib oder Gesundheit, nach den Vorschriften des Produkthaftungsgesetzes sowie im Umfang einer vom AN übernommenen Garantie.</p>
    <p>(2) Bei leicht fahrlässiger Verletzung einer Pflicht, die wesentlich für die Erreichung des Vertragszwecks ist (Kardinalpflicht), ist die Haftung des AN der Höhe nach begrenzt auf den Schaden, der nach der Art des fraglichen Geschäfts vorhersehbar und typisch ist.</p>
    <p>(3) Eine weitergehende Haftung des AN besteht, soweit gesetzlich zulässig, nicht.</p>
    <p>(4) Die vorstehende Haftungsbeschränkung gilt auch für die persönliche Haftung der Mitarbeiter, Vertreter und Organe des AN.</p>
  </div>
  <div class="col para" style="left:227px;top:361px">
    <h4 style="margin-top:0"><span class="sec">§ 7</span>Geheimhaltung</h4>
    <p>(Beide Vertragsparteien verpflichten sich gegenseitig zur vertraulichen Behandlung aller ihr bei der Zusammenarbeit bekanntwerdenden Geschäftsinterna, soweit diese nicht offenkundig sind oder aufgrund gesetzlicher Verpflichtungen oder auf Anordnung eines Gerichtes oder einer Behörde offen gelegt werden müssen. Die Pflicht zu vertraulichen Behandlung besteht auch über die Dauer des Vertragsverhältnisses hinaus.</p>
    <h4><span class="sec">§ 8</span>Abwerbungs- und Beschäftigungsverbot</h4>
    <p>(1) Die Vertragspartner verpflichten sich, während der Dauer des Projektes bzw. der Dauer der festgelegten Zusammenarbeit sowie innerhalb eines Jahres nach dessen Beendigung keine Mitarbeiter</p>
  </div>
  <div class="col para" style="left:420px;top:361px">
    <p>des anderen Vertragspartners abzuwerben oder zu beschäftigen, und zwar gleichgültig ob als Angestellte, freie Mitarbeiter oder eines beauftragten dritten Unternehmens. Das Abwerbe- und Beschäftigungsverbot gilt für alle abhängigen oder verbundenen Unternehmen des AG und analog des AN.</p>
    <p>(2) Verstößt eine Vertragspartei gegen vorstehende Regelung, so hat sie für jeden Fall der Zuwiderhandlung eine Vertragsstrafe in Höhe von € 15.000,00 an die andere Vertragspartei zu zahlen. Schadenersatzansprüche bleiben hiervon unberührt.</p>
    <h4><span class="sec">§ 9</span>Referenznennung</h4>
    <p>Der AN ist berechtigt, den AG als Referenzkunden zu benennen.</p>
  </div>
</section>

<section class="page terms">
  <div class="band" style="top:0">VERTRAGSBESTANDTEILE</div>
  <div class="abs deco-flowers" role="img" aria-label="Foto: weiße Margeriten mit grünen Blättern"></div>
  <div class="abs deco-pot" role="img" aria-label="Foto: mintgrüne Teekanne"></div>
  <div class="abs deco-note" role="img" aria-label="Foto: weißes Notizbuch mit mintgrünem Band"></div>
  <div class="abs terms-text">
    <p style="margin-top:0;font-weight:600">§ 10 Sonstige Bestimmungen</p>
    <p><b>(1)</b> Mündliche Nebenabreden zu diesem Vertrag bestehen nicht.</p>
    <p><b>(2)</b> Änderungen und/oder Ergänzungen zu diesem Vertrag bedürfen zu ihrer Wirksamkeit der Schriftform. Mündliche Vereinbarungen über die Aufhebung der Schriftform sind nichtig.</p>
    <p><b>(3)</b> Sollten einzelne Bestimmungen dieses Vertrages ganz oder teilweise unwirksam oder undurchführbar sein oder werden, so wird hierdurch die Gültigkeit der übrigen Bestimmungen nicht berührt. Anstelle der unwirksamen oder undurchführbaren Bestimmung ist eine neue wirksame und durchführbare Bestimmung in gehöriger Form zu vereinbaren, die dem Zweck der unwirksamen Bestimmung möglichst nahekommt. Das gleiche gilt im Falle einer Regelungslücke mit der Maßgabe, dass eine neue wirksame und durchführbare Bestimmung in gehöriger Form zu vereinbaren ist, die dem entspricht, was die Vertragsparteien zum Zeitpunkt des Vertragsschlusses geregelt haben würden, wenn sie die Lückenhaftigkeit erkannt hätten.</p>
    <p><b>(4)</b> Erfüllungsort und Gerichtsstand ist Bamberg</p>
  </div>
  <div class="abs sign" style="top:664px">Vertragsbestandteile gelesen, akzeptiert und Auftrag erteilt.</div>
  <div class="abs sign" style="top:724px">Ort, Datum: <span class="rule" style="width:298px"></span></div>
  <div class="abs sign" style="top:784px">Unterschrift Auftraggeber: <span class="rule" style="width:225px"></span></div>
</section>

<!-- Profile page -->
<section class="page profile">
  <div class="band" style="top:0">VERTRAGSBESTANDTEILE</div>
  <div class="abs profile-photo" role="img" aria-label="Foto: Geschäftsführerin in weißer Bluse im Büro"></div>
  <div class="abs profile-lead">Ihre Vertriebsagentur mit Know How und Unterstützung in</div>
  <div class="circle" style="left:41px"></div>
  <div class="circle" style="left:121px"></div>
  <div class="circle" style="left:222px"></div>
  <div class="circle" style="left:319px"></div>
  <div class="circle" style="left:411px"></div>
  <div class="abs profile-list">
    <div class="hi" style="font-weight:600;font-size:12px">BtoB</div>
    <div>- aktive Kundenbetreuung und -informationen</div>
    <div>- Kundenbefragungen mit Mehrwert</div>
    <div>- dynamische und automatisierte Leadgenerierung und Betreuung</div>
    <div class="hi">- BtoB Kundenimpuls®</div>
    <div class="in">Weg von der Kaltakquise –Wer sucht online gezielt nach Ihrer Dienstleistung?</div>
    <div class="in">Wir wissen wo, wie und wann – wir bleiben automatisiert und persönlich an Ihren Kunden dran und begeistern sie!</div>
    <div class="hi">- brinko-Checker®</div>
    <div class="in">Der neue Weg zur Leadgenerierung im BtoB Vertrieb.</div>
    <div class="in">Den ersten Testmonat gratis.</div>
  </div>
  <div class="abs portrait">Portrait</div>
  <div class="abs footer">
    <div class="name">brinko handel</div>
    <div class="addr">Name Straße PLZ Ort Telefonnummer website</div>
  </div>
</section>

</body>
</html>
```